BSWC Steadwell Foot Health Care

Steadwell Foot Health Care guarantees to treat your foot problems in one visit or we will provide a free treatment session to you until you are completely satisfied.

10% discount for all new patients!

Mobile foot care at home!

Professional and fully qualified and insured foot health care practitioner

Expert advice

How to care for your feet

Treatments; Diabetic foot health, Corns, Callouses, Fungal Infections, Verrucas, Cracked Heels, Ingrowing Toenails, Ball of foot pain and Heel pain.

```html
<!DOCTYPE html>
<html lang="en">
<head>
<meta charset="utf-8">
<title>Steadwell Foot Health Care – Leaflets</title>
<link href="https://fonts.googleapis.com/css2?family=Anton&family=Archivo+Black&family=Lato:wght@400;700;900&display=swap" rel="stylesheet">
<style>
:root{
  --orange:#ef4a23;
  --orange-deep:#e8401c;
  --ink:#1b1b1b;
  --grey-text:#333;
  --band:#4b4e50;
  --paper:#ffffff;
  --skin:#e9b79d;
  --skin-light:#f3d5c4;
}
*{margin:0;padding:0;box-sizing:border-box}
html,body{width:1200px;height:816px;overflow:hidden;background:var(--paper)}
body{position:relative;font-family:'Lato',sans-serif;color:var(--ink)}
.leaflet{position:absolute;top:2px;width:570px;height:814px;overflow:hidden}
.leaflet--front{left:14px;background:linear-gradient(180deg,#d9d9d9 0,#f4f4f4 140px,#fff 240px)}
.leaflet--back{left:618px;background:linear-gradient(180deg,var(--orange-deep) 0,var(--orange) 300px,#f6a483 560px,#fbe4d8 730px)}
.abs{position:absolute}

/* front */
.feet-backdrop{left:0;top:300px;width:570px;height:430px;background:radial-gradient(ellipse at 60% 45%,#efefef 0,#f8f8f8 55%,#fff 100%)}
.headline-top{left:20px;top:30px;font-family:'Archivo Black',sans-serif;font-size:44px;color:var(--orange);letter-spacing:1px;line-height:1}
.headline-main{left:18px;top:66px;font-family:'Archivo Black',sans-serif;font-size:88px;color:var(--orange);letter-spacing:2px;line-height:1}
.tick-box{left:410px;top:30px;width:140px;height:120px}
.intro{left:20px;top:152px;font-size:18px;color:var(--grey-text)}
.call{left:20px;top:178px;font-family:'Anton',sans-serif;font-size:35px;line-height:1.1;color:var(--ink);white-space:nowrap}
.call em{font-style:normal;color:var(--orange)}
.guarantee{left:20px;top:232px;width:530px;font-size:18.5px;font-weight:900;line-height:23px}
.about{left:20px;top:318px;width:214px;font-size:15.5px;line-height:20.8px;color:var(--grey-text)}
.treatments{left:246px;top:315px;width:200px}
.treatments h3{font-size:15px;font-weight:700;line-height:20px;margin-bottom:5px}
.treatments ul{list-style:none}
.treatments li{font-size:15.5px;line-height:21px;display:flex;align-items:center;gap:4px}
.treatments li svg{width:18px;height:16px;flex:none}
.badge{left:476px;border-radius:50%}
.badge--round{top:344px;width:54px;height:54px;background:#2e7d3a;border:4px solid #c9a640}
.badge--bar{top:406px;width:60px;height:16px;left:473px;border-radius:2px;background:#2a3f9c}
.brand{left:26px;top:556px;width:280px}
.brand-mark{display:flex;align-items:center;gap:10px;font-family:'Archivo Black',sans-serif;font-size:28px;color:var(--ink)}
.brand-mark i{width:32px;height:32px;border-radius:50%;background:var(--orange);display:block}
.brand-name{margin-top:10px;font-family:'Archivo Black',sans-serif;font-size:24px;line-height:28px;color:var(--orange)}
.offer{border-radius:50%;background:var(--orange);border:6px solid #fff;box-shadow:0 0 0 1px #ddd;color:#fff;text-align:center;display:flex;flex-direction:column;align-items:center;justify-content:center}
.offer--front{left:313px;top:513px;width:216px;height:216px;padding-bottom:6px}
.offer .claim{font-size:19px;line-height:1}
.offer .big{font-size:37px;font-weight:400;line-height:1.05}
.offer .mid{font-size:26px;line-height:1}
.offer .small{font-size:14px;line-height:1.2;margin-top:4px}
.offer .note{font-size:14px;line-height:1.3;color:var(--ink);margin-top:8px}
.band{left:0;bottom:0;width:570px;height:84px;background:var(--band);color:#fff;font-family:'Anton',sans-serif;font-size:33px;display:flex;align-items:center;justify-content:center;letter-spacing:.3px}

/* back */
.feet-photo{left:0;top:360px;width:570px;height:370px;background:linear-gradient(180deg,rgba(233,183,157,0) 0,var(--skin-light) 30%,var(--skin) 65%,#d49a7f 100%)}
.back-mark{left:0;top:36px;width:570px;display:flex;justify-content:center;align-items:center;gap:12px;font-family:'Archivo Black',sans-serif;font-size:30px;color:#fff}
.back-mark i{width:40px;height:40px;border-radius:50%;background:#fff;display:block}
.back-name{left:0;top:100px;width:570px;text-align:center;font-family:'Archivo Black',sans-serif;color:#fff;line-height:1}
.back-name span{display:block;font-size:50px}
.back-name small{display:block;font-size:32px;margin-top:8px}
.tagline{left:44px;top:246px;width:500px;font-family:'Anton',sans-serif;font-size:70px;line-height:1;color:#fff;transform:skew(-8deg) rotate(-3deg);transform-origin:left bottom;white-space:nowrap}
.visit{left:0;top:330px;width:570px;text-align:center;font-size:18px;line-height:21px;color:var(--ink)}
.offer--back{left:307px;top:490px;width:204px;height:204px}
.offer--back .claim{font-size:19px}
.offer--back .big{font-size:62px;line-height:1}
.offer--back .mid{font-size:25px}
.offer--back .small{font-size:16px;margin-top:2px}
.offer--back .tiny{font-size:12px;line-height:1.2}
</style>
</head>
<body>

<section class="leaflet leaflet--front">
  <div class="abs feet-backdrop" role="img" aria-label="Soft faded photograph of raised bare feet"></div>

  <h1 class="abs headline-top">FOOT PROBLEMS</h1>
  <div class="abs headline-main">SOLVED</div>
  <svg class="abs tick-box" viewBox="0 0 140 120" aria-hidden="true">
    <polygon points="14,72 96,72 104,112 22,112" fill="#fff" stroke="#333" stroke-width="5"/>
    <path d="M30,74 L54,102 L136,4 L124,0 L52,84 L40,68 Z" fill="var(--orange)"/>
  </svg>

  <p class="abs intro">New mobile foot care at home is now available in your area</p>
  <p class="abs call"><em>CALL NOW</em> to register 07700 900123</p>
  <p class="abs guarantee">BSWC, Steadwell Foot Health Care guarantees to treat your foot problems in one visit or we will provide a free treatment session to you until you’re completely satisfied.</p>

  <p class="abs about">From as little as £30 per treatment session our fully qualified and insured Foot Health Care Practitioner will immediately bring you pain relief while also offering you professional expert advice on how to care for your feet and keep them looking good all year round.</p>

  <div class="abs treatments">
    <h3>We have treatments for<br>and accurate diagnosis of:</h3>
    <ul>
      <li><svg viewBox="0 0 18 16"><rect x="1" y="7" width="10" height="8" fill="none" stroke="#333" stroke-width="1.5"/><path d="M3,8 L7,13 L17,1" fill="none" stroke="var(--orange)" stroke-width="2.6"/></svg>Corns <svg viewBox="0 0 18 16"><rect x="1" y="7" width="10" height="8" fill="none" stroke="#333" stroke-width="1.5"/><path d="M3,8 L7,13 L17,1" fill="none" stroke="var(--orange)" stroke-width="2.6"/></svg>Calluses</li>
      <li><svg viewBox="0 0 18 16"><rect x="1" y="7" width="10" height="8" fill="none" stroke="#333" stroke-width="1.5"/><path d="M3,8 L7,13 L17,1" fill="none" stroke="var(--orange)" stroke-width="2.6"/></svg>Fungal Infections</li>
      <li><svg viewBox="0 0 18 16"><rect x="1" y="7" width="10" height="8" fill="none" stroke="#333" stroke-width="1.5"/><path d="M3,8 L7,13 L17,1" fill="none" stroke="var(--orange)" stroke-width="2.6"/></svg>Verruca’s</li>
      <li><svg viewBox="0 0 18 16"><rect x="1" y="7" width="10" height="8" fill="none" stroke="#333" stroke-width="1.5"/><path d="M3,8 L7,13 L17,1" fill="none" stroke="var(--orange)" stroke-width="2.6"/></svg>Cracked Heels</li>
      <li><svg viewBox="0 0 18 16"><rect x="1" y="7" width="10" height="8" fill="none" stroke="#333" stroke-width="1.5"/><path d="M3,8 L7,13 L17,1" fill="none" stroke="var(--orange)" stroke-width="2.6"/></svg>In Growing Toenails</li>
      <li><svg viewBox="0 0 18 16"><rect x="1" y="7" width="10" height="8" fill="none" stroke="#333" stroke-width="1.5"/><path d="M3,8 L7,13 L17,1" fill="none" stroke="var(--orange)" stroke-width="2.6"/></svg>Diabetic Foot Health</li>
      <li><svg viewBox="0 0 18 16"><rect x="1" y="7" width="10" height="8" fill="none" stroke="#333" stroke-width="1.5"/><path d="M3,8 L7,13 L17,1" fill="none" stroke="var(--orange)" stroke-width="2.6"/></svg>Ball of Foot Pain</li>
      <li><svg viewBox="0 0 18 16"><rect x="1" y="7" width="10" height="8" fill="none" stroke="#333" stroke-width="1.5"/><path d="M3,8 L7,13 L17,1" fill="none" stroke="var(--orange)" stroke-width="2.6"/></svg>Heel Pain</li>
    </ul>
  </div>

  <div class="abs badge badge--round" aria-hidden="true"></div>
  <div class="abs badge badge--bar" aria-hidden="true"></div>

  <div class="abs brand">
    <div class="brand-mark"><i></i>BSWC</div>
    <div class="brand-name">Steadwell<br>Foot Health Care</div>
  </div>

  <div class="abs offer offer--front">
    <span class="claim">CLAIM</span>
    <span class="big">10% OFF</span>
    <span class="mid">TREATMENTS</span>
    <span class="small">WITH THIS LEAFLET</span>
    <span class="note">Specialists in Diabetic<br>Foot Health and<br>Elderly Foot Care</span>
  </div>

  <div class="abs band">PLACE YOUR FEET IN EXPERT HANDS</div>
</section>

<section class="leaflet leaflet--back">
  <div class="abs feet-photo" role="img" aria-label="Photograph of many bare feet raised together"></div>

  <div class="abs back-mark"><i></i>BSWC</div>
  <h2 class="abs back-name"><span>Steadwell</span><small>Foot Health Care</small></h2>

  <div class="abs tagline">We come to you!</div>
  <p class="abs visit">We will visit you in the comfort of your own home<br>or place of work whichever you find more convenient.</p>

  <div class="abs offer offer--back">
    <span class="claim">CLAIM</span>
    <span class="big">10%</span>
    <span class="mid">DISCOUNT</span>
    <span class="small">FOR ALL NEW<br>PATIENTS</span>
    <span class="tiny">WITH THIS<br>LEAFLET</span>
  </div>

  <div class="abs band">PLACE YOUR FEET IN EXPERT HANDS</div>
</section>

</body>
</html>
```